Project Lists Banner for HVAC ecommerce store

We want a banner that showcases our project list feature that will allow customers to create list of products that they can select and quickly order. this will be a middle of page banner. It will replace this banner - https://www.brightsnapclip.com/image/40872316
Font: Noto Sans
Size: 938x300 px
Color Options: #0059E, #00BBE3, #C6C8C7
Text:
Create lists of frequently purchased SKU's for fast ordering.
- Warehouse Inventory
- Complete Systems
- Large Projects
- And More...
"Sign In" is the call to action button. make button with non rounded (square) boarders.
We don't want a computer screen in banner nor a person. You can look at our competitors below for ideas.
Our staging server is lintvale7.com for reference
Our competitors:
https://www.hollowmarksupply.com/
https://www.tolvexo.com/
https://www.quibo.com/
https://www.vesko.com/index.html
Target Market(s)
HVAC, B2B
Industry/Entity Type
HVAC
Look and feel

```html
<!DOCTYPE html>
<html lang="en">
<head>
<meta charset="utf-8">
<title>Project Lists Banner</title>
<link href="https://fonts.googleapis.com/css2?family=Noto+Sans:wght@300;400;600;700&display=swap" rel="stylesheet">
<style>
:root{
  --stage:#e4e5e7;
  --navy:#0a3f7d;
  --navy-deep:#082f63;
  --blue:#0059a8;
  --blue-mid:#0b65b8;
  --cyan:#00bbe3;
  --ink:#1b2a44;
  --grey:#c6c8c7;
  --line:#dfe3e8;
  --muted:#6d7684;
  --white:#ffffff;
  --orange:#f07c1b;
}
*{box-sizing:border-box;margin:0;padding:0}
html,body{width:1200px;height:636px;overflow:hidden;background:var(--stage);font-family:"Noto Sans",sans-serif}
.banner{position:absolute;left:98px;top:152px;width:1007px;height:322px;overflow:hidden;background:var(--navy)}
.banner-backdrop{position:absolute;inset:0;width:100%;height:100%}
.headline{position:absolute;left:32px;top:30px;color:var(--white);font-weight:700;font-size:28px;line-height:33px;letter-spacing:.1px}
.features{position:absolute;left:34px;top:140px;list-style:none;color:var(--white);font-weight:300;font-size:22px}
.features li{position:relative;padding-left:28px;height:31px;line-height:31px}
.features li::before{content:"";position:absolute;left:0;top:10px;width:12px;height:12px;border-radius:50%;background:var(--cyan)}
.cta{position:absolute;left:33px;top:251px;width:201px;height:38px;background:var(--cyan);color:var(--ink);font-weight:700;font-size:24px;line-height:38px;text-align:center;letter-spacing:.5px;text-decoration:none}
.panel-shadow{position:absolute;left:475px;top:42px;width:488px;height:256px;background:var(--navy-deep)}
.panel{position:absolute;left:489px;top:35px;width:486px;height:241px;background:var(--white);color:var(--ink);font-size:5px;overflow:hidden}
.sidebar{position:absolute;left:0;top:0;width:95px;height:100%;border-right:1px solid var(--line)}
.sidebar h4{font-size:6.5px;font-weight:700;padding:10px 8px 8px;border-bottom:1px solid var(--line)}
.sidebar ul{list-style:none;padding:4px 8px}
.sidebar li{font-size:4.3px;line-height:7.5px;color:var(--muted);text-transform:uppercase}
.sidebar li.active{color:var(--blue)}
.import{position:absolute;left:5px;top:134px;width:86px;height:95px;border-top:1px solid var(--line)}
.import h5{font-size:5px;font-weight:700;padding:6px 4px 4px 12px;position:relative}
.import h5::before{content:"";position:absolute;left:3px;top:6px;width:6px;height:6px;background:#3a9a4c}
.dropzone{margin:0 6px;height:58px;border:1px dashed #9aa3ae;text-align:center;padding-top:5px;font-size:4.2px;line-height:5.5px;color:var(--muted)}
.btn-file{display:block;margin:3px auto;width:48px;height:8px;background:var(--blue);color:var(--white);font-size:4.3px;line-height:8px;font-weight:600}
.sample{color:var(--blue);text-decoration:underline}
.btn-tutorial{display:block;margin:4px auto 0;width:48px;height:9px;background:var(--orange);color:var(--white);font-size:4.3px;line-height:9px;text-align:center}
.main{position:absolute;left:101px;top:0;right:6px;height:100%}
.main h3{font-size:8px;font-weight:600;padding-top:7px}
.print{position:absolute;right:2px;top:9px;font-size:4.5px;color:var(--blue)}
.project-bar{margin-top:14px;height:11px;background:var(--blue);color:var(--white);font-size:5.5px;font-weight:700;line-height:11px;padding:0 5px;position:relative}
.project-bar span{position:absolute;right:6px;font-size:4.3px;font-weight:400}
.field{position:absolute;height:12px;border:1px solid var(--line);font-size:4.3px;line-height:10px;padding-left:5px;color:var(--muted)}
.add-btn{position:absolute;left:131px;top:118px;width:38px;height:13px;background:#8fb3d9;color:var(--white);font-size:4.5px;line-height:13px;text-align:center}
.apply-btn{position:absolute;right:2px;top:118px;width:33px;height:13px;background:var(--blue);color:var(--white);font-size:4.8px;font-weight:600;line-height:13px;text-align:center}
.table{position:absolute;left:0;right:0;top:146px}
.row{position:relative;height:20px;border-bottom:1px solid var(--line)}
.row.head{height:9px;font-weight:600;font-size:4.3px;color:var(--ink)}
.row .check{position:absolute;left:5px;top:7px;width:5px;height:5px;border:1px solid #9aa3ae}
.row.head .check{top:2px}
.row .brand{position:absolute;left:16px;top:6px;display:flex;align-items:center;gap:1px;font-size:3.4px;font-weight:700;color:var(--blue)}
.row .brand i{display:block;width:3px;height:3px;background:var(--blue)}
.row .name{position:absolute;left:35px;top:4px;font-size:4.3px;font-weight:600}
.row .sku{position:absolute;left:35px;top:10px;font-size:3.6px;color:var(--muted);font-weight:400}
.row.head .c{position:absolute;top:1px}
.qty{position:absolute;left:242px;top:4px;display:flex;gap:2px}
.qty b{width:12px;height:12px;background:#4c5561;color:var(--white);font-size:6px;line-height:12px;text-align:center;font-weight:400}
.qty em{width:12px;height:12px;font-style:normal;font-size:4px;line-height:12px;text-align:center}
.sell{position:absolute;left:297px;top:8px;font-size:4px}
.mine{position:absolute;left:334px;top:4px;font-size:4px;display:flex;gap:2px;align-items:center}
.mine span{width:25px;height:11px;border:1px solid var(--line);line-height:9px;padding-left:2px}
.trash{position:absolute;left:369px;top:7px;width:4px;height:5px;background:#4c5561}
</style>
</head>
<body>
<section class="banner" aria-label="Project lists promotion">
  <svg class="banner-backdrop" viewBox="0 0 1007 322" preserveAspectRatio="none">
    <defs>
      <linearGradient id="warehouse-tone" x1="0" y1="0" x2="1" y2="1">
        <stop offset="0" stop-color="#0d4a8c"/>
        <stop offset=".5" stop-color="#0a3f7d"/>
        <stop offset="1" stop-color="#07356c"/>
      </linearGradient>
    </defs>
    <rect width="1007" height="322" fill="url(#warehouse-tone)" role="img" aria-label="Faint warehouse interior in deep blue"/>
    <polygon points="282,322 672,0 1007,0 1007,322" fill="var(--cyan)"/>
    <polygon points="470,322 1007,55 1007,322" fill="var(--blue-mid)"/>
  </svg>

  <h1 class="headline">Create lists<br>of&nbsp; frequently purchased SKU's<br>for fast ordering.</h1>
  <ul class="features">
    <li>Warehouse Inventory</li>
    <li>Complete Systems</li>
    <li>Large Projects And More...</li>
  </ul>
  <a class="cta" href="#">SIGN IN</a>

  <div class="panel-shadow"></div>
  <div class="panel">
    <aside class="sidebar">
      <h4>My Account</h4>
      <ul>
        <li>Dashboard</li><li>Profile</li><li>Address Book</li><li>Manage Users</li>
        <li>Invoice History</li><li>Order History</li><li>Statements</li><li>My Quotes</li>
        <li>Favorites</li><li class="active">Project Lists</li>
      </ul>
      <div class="import">
        <h5>Import Project Lists</h5>
        <div class="dropzone">Drag and drop a .CSV file here, or<br>select file from your computer
          <span class="btn-file">Choose File</span>
          <span class="sample">Download Sample CSV</span>
        </div>
        <span class="btn-tutorial">Tutorial</span>
      </div>
    </aside>
    <div class="main">
      <h3>Project Lists</h3>
      <span class="print">Print Project</span>
      <div class="project-bar">Project:<span>Add New Project</span></div>
      <div class="field" style="left:2px;top:52px;width:188px">Main</div>
      <div class="field" style="left:2px;top:84px;width:190px;height:14px">Main</div>
      <div class="field" style="left:196px;top:84px;width:181px;height:22px"></div>
      <div class="field" style="left:0;top:118px;width:128px;height:13px">Enter Product Name or SKU to Add</div>
      <span class="add-btn">Add to List</span>
      <div class="field" style="left:296px;top:118px;width:48px;height:13px">Select Action</div>
      <span class="apply-btn">Apply</span>
      <div class="table">
        <div class="row head"><i class="check"></i><span class="c" style="left:18px">Product/SKU</span><span class="c" style="left:262px">Qty</span><span class="c" style="left:297px">Sell Price</span><span class="c" style="left:334px">My Price</span></div>
        <div class="row"><i class="check"></i><span class="brand"><i></i>HALDEN</span><span class="name">Roll Guard 6.5/10.5 Ranger</span><span class="sku">HX8017</span><span class="qty"><b>−</b><em>1</em><b>+</b></span><span class="sell">$413.00</span><span class="mine">$<span>413.00</span></span><i class="trash"></i></div>
        <div class="row"><i class="check"></i><span class="brand"><i></i>HALDEN</span><span class="name">Screwdriver, Combo, 6-In-1</span><span class="sku">HX9-41</span><span class="qty"><b>−</b><em>1</em><b>+</b></span><span class="sell">$9.00</span><span class="mine">$<span>9.00</span></span><i class="trash"></i></div>
        <div class="row"><i class="check"></i><span class="brand"><i></i>HALDEN</span><span class="name">Hand Seamer, Trevan</span><span class="sku">HX2-5011</span><span class="qty"><b>−</b><em>10</em><b>+</b></span><span class="sell">$50.00</span><span class="mine">$<span>50.00</span></span><i class="trash"></i></div>
        <div class="row"><i class="check"></i><span class="brand"><i></i>HALDEN</span><span class="name">Condenser Mounting Brackets, 1/8" Steel, 600LB Per Pair</span><span class="sku">HX7-AC2</span><span class="qty"><b>−</b><em>1</em><b>+</b></span><span class="sell">$31.00</span><span class="mine">$<span>31.00</span></span><i class="trash"></i></div>
      </div>
    </div>
  </div>
</section>
</body>
</html>
```